Etikett für eine Weinflasche gesucht
Zielgruppe
Guten zusammen wir brauchen ein Etikett für eine Weinflasche, die original Falsche ist im Anhang zu sehen, das Label soll 10,5cm hoch und 6,5cm breit sein, auf jeder Seite müssen 2,5mm für den Druck sein, also links, rechts, oben und unten.
-Es geht um einen süßen weiß Wein, Hauptzielgruppe werden Frauen sein, junge Frauen die den Wein eiskalt genießen.
-Es soll schlicht und edel werden und nicht zu überladen
-nichts anstößiges oder so, keine halbnackten Frauen z.B.
-aktuell sind zwei Sachen fix die ich habe möchte der Name soll 'Perla' heißen und es soll 'Moscato D Asti' drauf.
-bei einigen Punkten würde ich auf ihr Fachwissen vertrauen, ich überlege das Ganze unter Captain-Fell zu machen, dazu müsste das Logo drauf, ich bin mir aber nicht sicher, ist also kein muss
-zweiter Punkt wo ich unsicher bin, ich weiß noch nicht ob ich unter Perla noch den Slogan 'for Woman' schreiben soll, könnte mir das gut vorstellen, weiß aber nicht ob das zu sehr einschränkt wobei ich denke den Wein trinken zu 95% Frauen
Aufgabenstellung
Das Design soll edel wirken und eine gehobene, aber junge Zielgruppe ansprechen. Es handelt sich um einen süßen Weißwein, daher denken wir, dass er am ehesten Frauen ansprechen wird.

```html
<!DOCTYPE html>
<html lang="de">
<head>
<meta charset="utf-8">
<title>Perla – Moscato d'Asti Etikett</title>
<link rel="stylesheet" href="https://fonts.googleapis.com/css2?family=Open+Sans:wght@400;700&family=Dancing+Script:wght@500&family=Pinyon+Script&family=Questrial&display=swap">
<style>
  :root {
    --rose: #b85268;
    --kraft: #ded4c6;
    --kraft-light: #e6ddd1;
    --kraft-dark: #d4c8b8;
    --ink: #3b2416;
    --white: #ffffff;
    --page: #ffffff;
  }
  * { margin: 0; padding: 0; box-sizing: border-box; }
  html, body {
    width: 1200px;
    height: 1158px;
    overflow: hidden;
    background: var(--page);
  }
  .canvas {
    position: relative;
    width: 1200px;
    height: 1158px;
  }
  .label {
    position: absolute;
    left: 264px;
    top: 29px;
    width: 671px;
    height: 1100px;
    border-radius: 16px;
    overflow: hidden;
    background: radial-gradient(ellipse at 40% 35%, var(--kraft-light), var(--kraft) 55%, var(--kraft-dark));
  }
  .brand {
    position: absolute;
    top: 118px;
    left: 0;
    width: 100%;
    text-align: center;
    color: var(--ink);
  }
  .brand-name {
    font-family: "Open Sans", sans-serif;
    font-weight: 700;
    font-size: 58px;
    letter-spacing: 1px;
    line-height: 1;
  }
  .brand-tagline {
    display: flex;
    align-items: center;
    justify-content: center;
    gap: 14px;
    margin-top: 14px;
    font-family: "Open Sans", sans-serif;
    font-weight: 400;
    font-size: 28px;
    letter-spacing: 1px;
  }
  .brand-tagline .rule {
    width: 84px;
    height: 1px;
    background: var(--ink);
  }
  .wine-name {
    position: absolute;
    left: -38px;
    top: 230px;
    font-family: "Dancing Script", cursive;
    font-weight: 500;
    font-size: 400px;
    line-height: 1;
    color: var(--rose);
    transform: rotate(-9deg);
    transform-origin: left center;
    white-space: nowrap;
  }
  .audience {
    position: absolute;
    right: 22px;
    top: 813px;
    font-family: "Open Sans", sans-serif;
    font-size: 36px;
    color: var(--ink);
  }
  .band {
    position: absolute;
    left: 0;
    bottom: 0;
    width: 100%;
    height: 230px;
    background: var(--rose);
    color: var(--white);
    text-align: center;
  }
  .taste {
    margin-top: 14px;
    font-family: "Pinyon Script", cursive;
    font-size: 96px;
    line-height: 1.1;
    letter-spacing: 4px;
  }
  .appellation {
    margin-top: 6px;
    font-family: "Questrial", sans-serif;
    font-size: 47px;
    letter-spacing: 0.5px;
  }
</style>
</head>
<body>
  <main class="canvas">
    <section class="label">
      <header class="brand">
        <div class="brand-name">CPT. FELL</div>
        <div class="brand-tagline"><span class="rule"></span>DAS ORIGINAL<span class="rule"></span></div>
      </header>
      <h1 class="wine-name">Perla</h1>
      <p class="audience">for woman</p>
      <footer class="band">
        <p class="taste">Lieblich</p>
        <p class="appellation">MOSCATO D ASTI</p>
      </footer>
    </section>
  </main>
</body>
</html>
```